Modern and Clean Web Re-Design Project

We have 2 companies in similar industries: Printing and Mail Preparation/Fulfillment. We prefer sites that are clean and easy to navigate.Our printing company, Harbourline Press Works' website, hpwgroup-example.ca is outdated needs revamping. We have rebranded our logo and are looking for a new design that is clean, modern and geared to other corporations and business in the downtown Toronto area. Our mailing company, The Parcel Loft (theparcelloft-example.ca) needs a website as well. This company is in the Direct Mail and letter shop business, which essentially is addressing/personalizing people's printed matter and preparing it for either the Canadian or US postal service. The Parcel Loft specializes in not-for-profit and corporate sectors.Please see our logos to get an idea of the colors and look we want. For all intensive purposes, the sites can look similar in design all we want is that each site has the appropriate corporate colors and is a bit different so they don't look identical as the two business run as separate corporations.The content of the website should be easily changed by our staff and we want it to be setup to optimized for SEO based on the keywords we want. We are looking for someone to work on this project immediately

After doing some thinking, I would like the site to be more modern but the non flash sites that I have seen so far Im finding life-less and while I want something clean, not overly busy and corporate looking, I dont want the design to be bland looking.

Please design with the previous specs in mind but with a twist as mentioned above.

Thanks
Dorian

Target Market(s)

See above

Industry/Entity Type

Printing

Requirements
Must have
• Must match the design and style of each respective logoSee the attached impage of the front of our offices to have an idea of our lookWe must be able to edit the content ourselves without any fancy programs or tools.Must be SEO optimized
Nice to have
• An online order form that can be emailed to us for quotes.....perhaps a page with a bunch of fields that have drop down menus....
Should not have
• Should not be overly busy. I want it to be clean and simple but informative without being hard to navigate

```html
<!DOCTYPE html>
<html lang="en">
<head>
<meta charset="utf-8">
<title>Harbourline Press Works</title>
<link href="https://fonts.googleapis.com/css2?family=Oswald:wght@500&family=Source+Sans+3:wght@300;400;600&display=swap" rel="stylesheet">
<style>
:root{
  --orange:#f47a20;
  --orange-light:#fbb127;
  --orange-deep:#f06a16;
  --red-orange:#e4531f;
  --brown:#9b7650;
  --ink:#2f2f2f;
  --text:#555;
  --muted:#777;
  --line:#dddddd;
  --footer:#f4f4f4;
  --white:#fff;
}
*{box-sizing:border-box;margin:0;padding:0}
html,body{width:981px;height:1200px;overflow:hidden;background:var(--white)}
body{font-family:"Source Sans 3",sans-serif;color:var(--text);position:relative}
.header{position:absolute;left:0;top:0;width:981px;height:123px}
.brand{position:absolute;left:44px;top:40px;display:flex;align-items:center;gap:10px}
.brand-dot{width:30px;height:30px;border-radius:50%;background:var(--orange)}
.brand-name{font-family:"Source Sans 3",sans-serif;font-weight:600;font-size:22px;color:var(--brown)}
.call{position:absolute;right:41px;top:20px;font-size:17px;color:var(--red-orange);letter-spacing:.3px}
.call strong{font-weight:400;font-size:24px}
.nav{position:absolute;right:41px;top:78px;display:flex;font-size:16.5px;color:var(--ink)}
.nav span{padding:0 16px;border-left:1px solid #cfcfcf;line-height:20px}
.nav span:first-child{border-left:none}
.nav span:last-child{padding-right:0}
.hero{position:absolute;left:0;top:123px;width:981px;height:400px;overflow:hidden}
.hero-photo{position:absolute;inset:0;background:linear-gradient(120deg,#55565c 0%,#2c2c33 35%,#403a3c 60%,#6a3b26 100%)}
.hero-panel{position:absolute;inset:0;background:linear-gradient(160deg,var(--orange-light) 0%,var(--orange) 60%,var(--orange-deep) 100%);clip-path:polygon(689px 0,981px 0,981px 400px,591px 400px)}
.hero-copy{position:absolute;left:697px;top:55px;width:262px;color:var(--white)}
.hero-title{font-family:"Oswald",sans-serif;font-weight:500;line-height:1.05}
.hero-title .l1{font-size:36px;display:block}
.hero-title .l2{font-size:27px;display:block}
.hero-copy p{font-size:13.5px;font-weight:300;line-height:21px;margin-top:8px}
.hero-btn{display:inline-block;margin-top:20px;background:var(--red-orange);font-family:"Oswald",sans-serif;font-size:14px;padding:6px 17px;color:var(--white)}
.dots{display:flex;gap:4px;margin-top:23px}
.dots i{width:10px;height:10px;border-radius:50%;background:rgba(255,255,255,.45)}
.dots i:first-child{background:var(--white)}
.cards{position:absolute;top:552px;left:46px;display:flex;gap:25px}
.card{width:281px;height:244px;border:1px solid #e2e2e2;box-shadow:1px 2px 3px rgba(0,0,0,.12);padding:17px 20px}
.card h3{font-family:"Oswald",sans-serif;font-weight:500;font-size:20px;color:var(--red-orange);line-height:22px}
.card-img{height:99px;margin-top:10px;border:1px solid #e4e4e4}
.img-mission{background:linear-gradient(100deg,#f7c23a,#ee5a2a 40%,#a04fc0 75%,#f2eaf7)}
.img-commercial{background:linear-gradient(120deg,#2a9ad8,#f05a2a 45%,#e8284a 65%,#2bb34a)}
.img-digital{background:linear-gradient(180deg,#9a9a9a,#d8d8d8 55%,#e9735a 70%,#5a8fd8 85%,#f4f4f4)}
.card p{font-size:13px;font-weight:300;line-height:18px;margin-top:9px;color:var(--text)}
.card .more{font-family:"Oswald",sans-serif;font-size:13.5px;color:var(--ink);margin-top:9px;display:block}
.welcome{position:absolute;left:45px;top:845px;width:570px}
.welcome h1{font-weight:400;font-size:25px;color:var(--ink);letter-spacing:-.3px}
.welcome h2{font-weight:400;font-size:15.5px;color:var(--ink);margin-top:10px}
.welcome p{font-size:13px;line-height:19.5px;color:var(--text);margin-top:6px}
.services{position:absolute;left:669px;top:845px;width:234px}
.services h2{font-weight:400;font-size:20px;color:var(--brown)}
.services ul{list-style:none;margin-top:8px}
.services li{display:flex;align-items:center;gap:8px;font-size:13px;color:var(--brown);height:28.5px;border-bottom:1px solid var(--line)}
.services li:last-child{border-bottom:none}
.footer{position:absolute;left:0;top:1084px;width:981px;height:116px;background:linear-gradient(#efefef,#fafafa 20%,#fff)}
.copy{position:absolute;left:45px;top:28px;font-size:11.5px;color:var(--text)}
.fnav{position:absolute;right:124px;top:27px;font-size:12.5px;color:var(--text)}
.fnav span{padding:0 8px;border-left:1px solid #999}
.fnav span:first-child{border-left:none}
.social{position:absolute;right:45px;top:25px;display:flex;gap:4px}
.social i{width:21px;height:21px;border-radius:3px}
.s1{background:#3aaee8}.s2{background:#1b7bb8}.s3{background:#3b5ea8}
</style>
</head>
<body>
<header class="header">
  <div class="brand"><span class="brand-dot"></span><span class="brand-name">Harbourline Press Works</span></div>
  <div class="call">CALL US <strong>416-555-0148</strong></div>
  <nav class="nav"><span>MAIN</span><span>WHAT ARE WE</span><span>WHAT WE DO</span><span>GALLERY</span><span>CONTACT US</span></nav>
</header>

<section class="hero">
  <div class="hero-photo" role="img" aria-label="Photo of the office reception area with lit signage and wooden desk"></div>
  <div class="hero-panel"></div>
  <div class="hero-copy">
    <h1 class="hero-title"><span class="l1">HARBOURLINE</span><span class="l2">PRESS WORKS</span></h1>
    <p>Phasellus felis dolor, scelerisque a, tempus eget, lobortis id, libero.</p>
    <p style="margin-top:6px">Donec scelerisque leo ac risus. Praesent sit amet est. In dictum, dolor eu dictum porttitor, enim felis viverra mi, eget luctus massa purus quis odio.</p>
    <span class="hero-btn">LEARN MORE</span>
    <div class="dots"><i></i><i></i><i></i><i></i></div>
  </div>
</section>

<section class="cards">
  <article class="card">
    <h3>OUR MISSION</h3>
    <div class="card-img img-mission" role="img" aria-label="Colourful illustration of business cards and print splashes"></div>
    <p>Nunc tempus felis vitae urna. Vivamus port-titor, g purus nisi eleifend libero</p>
    <span class="more">LEARN MORE</span>
  </article>
  <article class="card">
    <h3>COMMERCIAL PRINTING</h3>
    <div class="card-img img-commercial" role="img" aria-label="Photo of printed colour calendars and swatches"></div>
    <p>Nunc tempus felis vitae urna. Vivamus port-titor, g purus nisi eleifend libero</p>
    <span class="more">LEARN MORE</span>
  </article>
  <article class="card">
    <h3>DIGITAL PRINTING</h3>
    <div class="card-img img-digital" role="img" aria-label="Photo of a digital press printing colour sheets"></div>
    <p>Nunc tempus felis vitae urna. Vivamus port-titor, g purus nisi eleifend libero</p>
    <span class="more">LEARN MORE</span>
  </article>
</section>

<section class="welcome">
  <h1>WELCOME TO OUR WEBSITE MAINPAGE..</h1>
  <h2>Duis tincidunt lectus quis dui viverra vestibulum</h2>
  <p>Suspendisse vulputate aliquam dui. Nulla elementum dui ut augue. Aliquam vehicula mi at mauris. Maecenas placerat, nisl at consequat rhoncus, sem nunc gravida justo, quis eleifend arcu velit quis lacus. Morbi magna magna, tincidunt a, mattis non, imperdiet vitae, tellus.</p>
  <p>Phasellus felis dolor, scelerisque a, tempus eget, lobortis id, libero. Donec scelerisque leo ac risus. Praesent sit amet est. In dictum, dolor eu dictum porttitor, enim felis viverra mi, eget luctus massa purus quis odio.</p>
</section>

<aside class="services">
  <h2>SERVICES WE PROVIDE</h2>
  <ul>
    <li><svg width="14" height="12" viewBox="0 0 14 12"><polyline points="1,6 5,10 13,1" fill="none" stroke="#9b7650" stroke-width="2.6"/></svg>Maecenas aliquet velit vel turpis.</li>
    <li><svg width="14" height="12" viewBox="0 0 14 12"><polyline points="1,6 5,10 13,1" fill="none" stroke="#9b7650" stroke-width="2.6"/></svg>Mauris neque metus, malesuada nec</li>
    <li><svg width="14" height="12" viewBox="0 0 14 12"><polyline points="1,6 5,10 13,1" fill="none" stroke="#9b7650" stroke-width="2.6"/></svg>Porttitor mattis enim.</li>
    <li><svg width="14" height="12" viewBox="0 0 14 12"><polyline points="1,6 5,10 13,1" fill="none" stroke="#9b7650" stroke-width="2.6"/></svg>In massa libero interdum nec interdum</li>
    <li><svg width="14" height="12" viewBox="0 0 14 12"><polyline points="1,6 5,10 13,1" fill="none" stroke="#9b7650" stroke-width="2.6"/></svg>In ullamcorper est eget tempor cursus</li>
  </ul>
</aside>

<footer class="footer">
  <div class="copy">© 2013 Company Name.&nbsp; All right reserved.&nbsp; Term of Use</div>
  <nav class="fnav"><span>Main</span><span>What are we</span><span>What We Do</span><span>Gallery</span><span>Contact Us</span></nav>
  <div class="social"><i class="s1" role="img" aria-label="Social link"></i><i class="s2" role="img" aria-label="Social link"></i><i class="s3" role="img" aria-label="Social link"></i></div>
</footer>
</body>
</html>
```